Mini-Banner für Rubriken
Hallo,
wir benötigen für unsere Seite www.quilmar.de neue und vorallem passende Banner für die Highlights (rechte Seite) innerhalb der Rubriken, wie z.B. All Inklusive, Wellness, Urlaub an der Küste u.s.w. Vielen Dank für die Vorschläge !

```html
<!DOCTYPE html>
<html lang="de">
<head>
<meta charset="utf-8">
<title>Highlights – Mini-Banner Entwurf 3</title>
<link href="https://fonts.googleapis.com/css2?family=Noto+Sans:wght@400;700&family=Roboto+Condensed:wght@700&display=swap" rel="stylesheet">
<style>
  :root{
    --page:#ffffff;
    --box:#f1f0ee;
    --box-line:#c9c7c4;
    --head-top:#ececec;
    --head-bottom:#d7d7d7;
    --ink:#1d1d1d;
    --link:#9a1818;
    --price:#b3161a;
    --btn:#8a1d1e;
    --ring-blue:#0a6ebd;
    --ring-green:#86c03a;
    --lens:#f7f7f7;
    --band-bayern:#1b6fd2;
    --band-erz:#df1313;
    --band-harz:#4b7a1b;
    --band-kueste:#dc9a12;
  }
  *{box-sizing:border-box;margin:0;padding:0}
  html,body{width:1200px;height:910px;overflow:hidden;background:var(--page)}
  body{font-family:"Noto Sans",Verdana,sans-serif;color:var(--ink)}
  .stage{position:relative;width:931px;height:706px;transform:scale(1.28894);transform-origin:0 0;overflow:hidden;font-size:11.5px;line-height:1.3}
  .abs{position:absolute}

  .box{position:absolute;background:var(--box);border:1px solid var(--box-line);border-radius:4px;overflow:hidden}
  .box-head{height:23px;background:linear-gradient(var(--head-top),var(--head-bottom));border-bottom:1px solid var(--box-line);text-align:center;font-weight:700;font-size:12px;line-height:23px}
  .box-body{padding:8px 7px}
  .links{list-style:none;color:var(--link)}
  .links li::before{content:"• ";color:var(--link)}
  .red{color:var(--link)}

  .column-main{position:absolute;left:215px;top:0;width:497px;height:706px;background:#f8f8f8;border-left:1px solid #ddd;border-right:1px solid #ddd}
  .divider{position:absolute;left:8px;right:6px;height:2px;background:#555}
  .photo{position:absolute;border-radius:3px}
  .offer-title{position:absolute;color:var(--link);font-weight:700;font-size:14.5px}
  .offer-sub{position:absolute;color:var(--price);font-weight:700;font-size:12.5px}
  .offer-text{position:absolute;color:#444;font-size:11.5px}
  .price{position:absolute;right:18px;color:var(--price);font-weight:700;font-size:20px;white-space:nowrap}
  .price small{font-size:12px;margin-right:8px}
  .more-btn{position:absolute;width:124px;height:19px;background:linear-gradient(#a52425,var(--btn));border-radius:3px;color:#fff;font-weight:700;font-size:12px;text-align:center;line-height:19px}

  .banner{position:absolute;width:187px;height:60px;border:1px solid #222;overflow:hidden}
  .banner .scene{position:absolute;inset:0}
  .banner .band{position:absolute;left:0;right:0;bottom:0;height:13px;color:#fff;font-family:"Roboto Condensed","Arial Narrow",sans-serif;font-weight:700;font-size:10.5px;letter-spacing:.3px;text-align:right;padding-right:5px;line-height:13px}
  .band-bayern{background:var(--band-bayern)}
  .band-erz{background:var(--band-erz)}
  .band-harz{background:var(--band-harz)}
  .band-kueste{background:var(--band-kueste)}
  .scene-bayern{background:linear-gradient(#a9c9ea 0%,#d8e6f1 38%,#6f8d6a 55%,#5e86a8 75%,#3c6a8c 100%)}
  .scene-erz{background:linear-gradient(#3d8ee0 0%,#a9d3f4 40%,#8fc44a 60%,#5a8f25 100%)}
  .scene-harz{background:linear-gradient(#6b8f3a 0%,#86ab45 40%,#9ec25a 100%)}
  .scene-kueste{background:linear-gradient(#7fbde8 0%,#cfe6f5 45%,#eae0c6 70%,#d9c9a2 100%)}
  .badge{position:absolute;left:5px;top:4px;width:33px;height:33px;border-radius:50%;background:var(--band-erz);border:2px solid #fff;color:#fff;font-family:"Roboto Condensed",sans-serif;font-weight:700;text-align:center;font-size:11px;line-height:11px;padding-top:7px}
  .badge span{display:block;font-size:5px;line-height:7px}

  .draft-label{position:absolute;left:270px;top:480px;width:270px;text-align:center;font-family:"Roboto Condensed","Arial Narrow",sans-serif;font-weight:700;font-size:33px;letter-spacing:1.5px;color:#111}
</style>
</head>
<body>
<div class="stage">

  <!-- left column -->
  <div class="box" style="left:8px;top:-20px;width:188px;height:78px">
    <div class="box-body" style="padding-top:20px">
      <ul class="links"><li>love &amp; romance</li></ul>
      <ul class="links" style="margin-top:10px"><li>Alle Angebote</li></ul>
    </div>
  </div>

  <div class="box" style="left:8px;top:70px;width:188px;height:123px">
    <div class="box-head">Gutschein schenken</div>
    <div role="img" aria-label="Gutschein-Grafik mit geschwungener Schrift auf rotem Grund" style="margin:2px 1px;height:94px;background:linear-gradient(135deg,#b9232b,#8c141b)"></div>
  </div>

  <div class="box" style="left:8px;top:208px;width:188px;height:78px">
    <div class="box-head"></div>
    <div class="box-body" style="padding-top:10px">
      <ul class="links"><li>Rückruf anfordern</li><li>Anfrage stellen</li></ul>
    </div>
  </div>

  <div class="box" style="left:8px;top:295px;width:188px;height:190px">
    <div class="box-head">Newsletter</div>
    <div class="box-body" style="line-height:1.25">
      Bleiben Sie immer auf dem neuesten Stand. Tragen Sie sich jetzt für unseren Newsletter ein.
      <div style="margin-top:10px">Email:<span style="display:inline-block;width:130px;height:17px;background:#fff;border:1px solid #888;vertical-align:middle;margin-left:2px"></span></div>
      <div style="margin:4px 0 0 49px;width:100px;height:19px;background:linear-gradient(#a52425,var(--btn));border-radius:3px;color:#fff;font-weight:700;text-align:center;line-height:19px;font-size:12px">Eintragen</div>
      <div class="red" style="text-align:center;margin-top:14px">Newsletter Abstellen</div>
    </div>
  </div>

  <div class="box" style="left:8px;top:497px;width:188px;height:230px">
    <div class="box-head">VIP Programm</div>
    <div class="box-body" style="line-height:1.2">
      <p>Bei einer Buchung erhalten Sie exklusive Sonder&shy;konditionen und verschiedene kostenfreie Upgrades als quilmar.de Kunde.</p>
      <p style="margin-top:12px">Legen Sie einfach bei Anreise im Hotel Ihre quilmar.de - VIP-Karte vor. Diese erhalten Sie mit Ihren Buchungs&shy;unterlagen.</p>
      <div role="img" aria-label="VIP-Karte" style="margin-top:10px;height:20px;background:linear-gradient(#e9d9a8,#c8a85e)"></div>
    </div>
  </div>

  <!-- main column -->
  <div class="column-main">
    <div class="photo" role="img" aria-label="Hotelrestaurant mit gedeckten Tischen" style="left:13px;top:-10px;width:167px;height:100px;background:linear-gradient(#c7a784,#8d4a33 60%,#b22a22)"></div>
    <p class="offer-text" style="left:268px;top:-3px;width:215px">entspricht den Erwartungen eines 4 Sterne Hauses. Gro…</p>
    <div class="price" style="top:40px"><small>schon ab</small>199,00 € p.P.</div>
    <div class="more-btn" style="left:355px;top:70px">mehr Infos...!</div>
    <div class="divider" style="top:108px"></div>

    <div class="offer-title" style="left:14px;top:122px">Bad Wellness in der Seenlandschaft</div>
    <div class="photo" role="img" aria-label="Hotelansicht" style="left:245px;top:170px;width:214px;height:143px;background:linear-gradient(#7a8c99,#3f4b43)"></div>
    <div class="divider" style="top:333px"></div>

    <div class="offer-title" style="left:14px;top:381px">Kurzurlaub am Wasser grenzenlose</div>
    <p class="offer-text" style="left:14px;top:440px;width:470px;text-align:right">genau<br>d Feld,<br>see und</p>
    <div class="price" style="top:507px">ab 99,77 € p.P.</div>
    <div class="more-btn" style="left:355px;top:535px">mehr Infos...!</div>
    <div class="divider" style="top:574px"></div>

    <div class="offer-title" style="left:14px;top:587px">Wochenend-Auszeit zu Sonderkonditionen in der Altmark</div>
    <div class="offer-sub" style="left:14px;top:605px">2 ÜN von Freitag bis Sonntag inklusive Vollverpflegung &amp; Getränke</div>
    <p class="offer-text" style="left:16px;top:636px;width:215px;color:#555">Ein paar romantische Tage bringen Ihnen die gewünschte Entspannung. Im Einklang die Natur erleben. Spüren Sie die wohltuende Natur bei ausgedehnten …</p>
    <div class="photo" role="img" aria-label="Speisesaal mit Gemälden an der Wand" style="left:245px;top:633px;width:214px;height:80px;background:linear-gradient(#d8cfb3,#9a8a66)"></div>
  </div>

  <!-- right column -->
  <div class="box" style="left:730px;top:-20px;width:190px;height:68px">
    <div style="margin:36px 0 0 12px;width:160px;height:22px;background:#fff;border:1px solid #999;text-align:center;line-height:20px;font-size:12px">suchen</div>
  </div>

  <div class="box" style="left:730px;top:67px;width:190px;height:298px">
    <div class="box-head">Highlights</div>
  </div>

  <div class="banner" style="left:731px;top:95px"><div class="scene scene-bayern" role="img" aria-label="Bergsee vor Alpenpanorama"></div><div class="band band-bayern">WELLNESS URLAUB IN BAYERN</div></div>
  <div class="banner" style="left:731px;top:159px"><div class="scene scene-erz" role="img" aria-label="Sonnige Wiese unter blauem Himmel"></div><div class="badge">ALL<span>INCLUSIVE</span></div><div class="band band-erz">IM ERZGEBIRGE</div></div>
  <div class="banner" style="left:731px;top:223px"><div class="scene scene-harz" role="img" aria-label="Entspannung im Gras"></div><div class="band band-harz">ERHOLUNG IM HARZ</div></div>
  <div class="banner" style="left:731px;top:287px"><div class="scene scene-kueste" role="img" aria-label="Liegestühle am Strand"></div><div class="band band-kueste">URLAUB AN DER KÜSTE</div></div>

  <div class="box" style="left:730px;top:378px;width:190px;height:225px">
    <div class="box-head">quilmar Telefon Support</div>
    <div class="box-body" style="line-height:1.25">
      <p>Sie möchten dieses Angebot telefonisch buchen oder wünschen eine persönliche Beratung? Sie erreichen uns von Montag-Freitag von 08:00 - 17:00 Uhr</p>
      <p style="margin-top:12px">unter</p>
      <p style="margin-top:8px;font-weight:700">quilmar <span class="red">FREECALL</span><br>(D) 0800 - 31 72 904<br>oder per Email<br><span class="red">info@quilmar.de</span></p>
    </div>
  </div>

  <div class="box" style="left:730px;top:615px;width:190px;height:110px">
    <div class="box-head">Hotel Übersicht</div>
    <div role="img" aria-label="Deutschlandkarte mit Hotelstandorten" style="margin:12px 7px 0;height:70px;background:linear-gradient(#f2f2f2,#dedede)"></div>
  </div>

  <!-- magnifier: tail base sits inside the disc so it flows smoothly into the ring -->
  <svg class="abs" style="left:0;top:0" width="931" height="706" viewBox="0 0 931 706" aria-hidden="true">
    <path d="M731 96 L540 140 L645 305 Z" fill="var(--ring-blue)"/>
    <circle cx="406" cy="355" r="266" fill="var(--ring-blue)"/>
    <circle cx="406" cy="355" r="252" fill="var(--ring-green)"/>
    <circle cx="406" cy="355" r="238" fill="var(--lens)"/>
  </svg>

  <div class="banner" style="left:305px;top:198px"><div class="scene scene-bayern" role="img" aria-label="Bergsee vor Alpenpanorama"></div><div class="band band-bayern">WELLNESS URLAUB IN BAYERN</div></div>
  <div class="banner" style="left:305px;top:263px"><div class="scene scene-erz" role="img" aria-label="Sonnige Wiese unter blauem Himmel"></div><div class="badge">ALL<span>INCLUSIVE</span></div><div class="band band-erz">IM ERZGEBIRGE</div></div>
  <div class="banner" style="left:305px;top:328px"><div class="scene scene-harz" role="img" aria-label="Entspannung im Gras"></div><div class="band band-harz">ERHOLUNG IM HARZ</div></div>
  <div class="banner" style="left:305px;top:393px"><div class="scene scene-kueste" role="img" aria-label="Liegestühle am Strand"></div><div class="band band-kueste">URLAUB AN DER KÜSTE</div></div>

  <div class="draft-label">ENTWURF 3</div>
</div>
</body>
</html>
```